Professional Business Card for Commercial Cleaning Company

We need a business card that represents our commercial janitorial cleaning company and represent several brands for our company so we do not want to highlight the logo too much. We want something that says we are professional.
Notes:No website or address as we have many locations and many websites and companies under our corporate name of "Brightmere Holdings, LLC" . Every time we hand a customer a business card they have contacted us via another brand we own but we don't want to have 21 business cards so we want to not focus on Brightmere Holdings, LLC too much since people will automatically ask "What is Brightmere Holdings, LLC" Example: Noodle Barn and Wrap Lodge restaurants are owned by "Zest! Brands" is the corporation name. Same principle here. Except we do not advertise at this time that all of our brands are connected. Hope this helps.
Target Market(s)
Commercial Cleaning
Industry/Entity Type
Janitorial Service
Contact Information for Business Card
Miles Penrow
Business Development
482-639-2274
sales@brightmereholdingsllc.example
Requirements
Must have
- Logo with contact information, need to be able to easily edit contact info for others in my office.
Nice to have
- Professional Image. Like to see a colorful bold look and a more standard business card look.
Should not have
- Any type of cleaning icons, tools, people or water.

```html
<!DOCTYPE html>
<html lang="en">
<head>
<meta charset="utf-8">
<title>Brightmere Holdings, LLC — Business Card</title>
<link href="https://fonts.googleapis.com/css2?family=Overpass:wght@400;700;800&display=swap" rel="stylesheet">
<style>
  :root {
    --backdrop: #333333;
    --paper: #ffffff;
    --navy: #003876;
    --blue: #0a93d0;
    --green: #6a9f32;
    --lime: #aed23a;
  }
  * { margin: 0; padding: 0; box-sizing: border-box; }
  html, body {
    width: 1200px;
    height: 1200px;
    overflow: hidden;
    background: var(--backdrop);
    font-family: "Overpass", Arial, sans-serif;
  }
  .card {
    position: absolute;
    left: 260px;
    width: 680px;
    height: 416px;
    background: var(--paper);
    overflow: hidden;
  }
  .card--front { top: 146px; }
  .card--back { top: 686px; }

  .brand-name {
    position: absolute;
    left: 0;
    right: 0;
    text-align: center;
    color: var(--navy);
    font-weight: 800;
    letter-spacing: -0.5px;
    white-space: nowrap;
  }
  .card--front .brand-name { top: 182px; font-size: 42px; line-height: 52px; }
  .card--back .brand-name { top: 44px; font-size: 30px; line-height: 38px; }

  .accent-band {
    position: absolute;
    left: 0;
    right: 0;
    bottom: 0;
    height: 52px;
    background: linear-gradient(90deg, var(--navy) 0%, var(--blue) 45%, var(--green) 75%, var(--lime) 100%);
  }

  .contact {
    position: absolute;
    right: 50px;
    top: 148px;
    list-style: none;
    text-align: right;
    color: var(--navy);
  }
  .contact__line {
    position: relative;
    padding-right: 28px;
    white-space: nowrap;
  }
  .contact__line::after {
    content: "";
    position: absolute;
    right: 0;
    top: 50%;
    width: 12px;
    height: 12px;
    margin-top: -7px;
    background: var(--green);
  }
  .contact__line--name,
  .contact__line--role {
    font-weight: 800;
    font-size: 18px;
    line-height: 28px;
  }
  .contact__line--phone,
  .contact__line--email {
    font-weight: 400;
    font-size: 16px;
    line-height: 29px;
  }
  .contact__line--phone { margin-top: 41px; }
</style>
</head>
<body>

  <section class="card card--front" aria-label="Card front">
    <p class="brand-name">Brightmere Holdings, LLC</p>
  </section>

  <section class="card card--back" aria-label="Card back">
    <div class="accent-band" role="img" aria-label="Decorative colour band in navy, blue and green"></div>

    <p class="brand-name">Brightmere Holdings, LLC</p>

    <ul class="contact">
      <li class="contact__line contact__line--name">Miles Penrow</li>
      <li class="contact__line contact__line--role">Business Development</li>
      <li class="contact__line contact__line--phone">482-639-2274</li>
      <li class="contact__line contact__line--email">sales@brightmereholdingsllc.example</li>
    </ul>
  </section>

</body>
</html>
```